Business Card Design for Property Development Company Director

I am looking for a professional and unforgettable business card design for our Director of our Property Development Company.
Please see attached .pptx file to find out what information to include. You don't have to follow the exact format shown in the file - I am interested to see your creative flair using the information provided.

```html
<!DOCTYPE html>
<html lang="en">
<head>
<meta charset="UTF-8">
<title>Harwell Property Group – Business Card</title>
<link href="https://fonts.googleapis.com/css2?family=Arimo:wght@400;700&display=swap" rel="stylesheet">
<style>
  :root {
    --brand-blue: #0d56a6;
    --brand-grey: #5f6063;
    --card-white: #ffffff;
    --backdrop: #e6e7ea;
    --text-white: #ffffff;
  }
  * { margin: 0; padding: 0; box-sizing: border-box; }
  html, body {
    width: 1200px; height: 800px; overflow: hidden;
    background: var(--backdrop);
    font-family: "Arimo", Arial, sans-serif;
  }
  .canvas {
    width: 1200px; height: 800px;
    display: flex; align-items: center; justify-content: center; gap: 48px;
  }
  .card {
    width: 520px; height: 300px; border-radius: 22px;
    position: relative; overflow: hidden;
    box-shadow: 0 10px 30px rgba(0,0,0,0.18);
  }

  /* Front: blue side */
  .card--front {
    background: var(--brand-blue); color: var(--text-white);
    display: flex; flex-direction: column; align-items: center; justify-content: center;
    text-align: center;
  }
  .tagline {
    font-weight: 700; font-size: 17px; line-height: 1.35; letter-spacing: 0.4px;
  }
  .brand {
    display: flex; align-items: center; gap: 14px; margin: 26px 0 30px;
  }
  .brand__square { width: 46px; height: 46px; background: var(--text-white); }
  .brand__text { text-align: left; font-weight: 700; color: var(--text-white); line-height: 1; }
  .brand__name { font-size: 40px; letter-spacing: 1px; display: block; }
  .brand__sub { font-size: 12px; letter-spacing: 4.2px; display: block; margin-top: 4px; }
  .invite { font-size: 11px; letter-spacing: 0.2px; }
  .invite strong { font-weight: 700; }

  /* Back: white side */
  .card--back { background: var(--card-white); }
  .contact-block { position: absolute; left: 38px; bottom: 34px; }
  .wordmark { color: var(--brand-blue); font-weight: 700; line-height: 1; margin-bottom: 22px; }
  .wordmark__name { font-size: 38px; letter-spacing: 0.5px; display: block; }
  .wordmark__sub { font-size: 12px; letter-spacing: 4.6px; display: block; margin-top: 3px; }
  .person__name { color: var(--brand-grey); font-weight: 700; font-size: 17px; letter-spacing: 0.3px; }
  .person__role { color: var(--brand-blue); font-size: 14px; margin-bottom: 10px; }
  .contact-list { list-style: none; font-size: 13px; color: var(--brand-grey); }
  .contact-list li { display: flex; align-items: center; gap: 8px; margin-bottom: 3px; }
  .contact-list svg { width: 12px; height: 12px; fill: var(--brand-blue); flex-shrink: 0; }
  .licence { color: var(--brand-blue); font-size: 12px; margin-top: 6px; }
  .feature-mark {
    position: absolute; right: 40px; top: 46px;
    width: 180px; height: 180px; background: var(--brand-blue);
  }
</style>
</head>
<body>
<main class="canvas">
  <section class="card card--front" aria-label="Business card front">
    <p class="tagline">PROPERTY DEVELOPMENT<br>&amp; SITE ACQUISITION SPECIALISTS</p>
    <div class="brand">
      <span class="brand__square" aria-hidden="true"></span>
      <div class="brand__text">
        <span class="brand__name">HARWELL</span>
        <span class="brand__sub">PROPERTY GROUP</span>
      </div>
    </div>
    <p class="invite">Ask me about our <strong>INVESTMENT &amp; PARTNERSHIP</strong> opportunities</p>
  </section>

  <section class="card card--back" aria-label="Business card back">
    <span class="feature-mark" aria-hidden="true"></span>
    <div class="contact-block">
      <div class="wordmark">
        <span class="wordmark__name">HARWELL</span>
        <span class="wordmark__sub">PROPERTY GROUP</span>
      </div>
      <p class="person__name">DANIEL MERCER</p>
      <p class="person__role">Director</p>
      <ul class="contact-list">
        <li>
          <svg viewBox="0 0 24 24" aria-hidden="true"><path d="M6.6 10.8a15 15 0 0 0 6.6 6.6l2.2-2.2a1 1 0 0 1 1-.25 11.4 11.4 0 0 0 3.6.57 1 1 0 0 1 1 1V20a1 1 0 0 1-1 1A17 17 0 0 1 3 4a1 1 0 0 1 1-1h3.5a1 1 0 0 1 1 1c0 1.25.2 2.45.57 3.57a1 1 0 0 1-.25 1z"/></svg>
          0400 123 456
        </li>
        <li>
          <svg viewBox="0 0 24 24" aria-hidden="true"><path d="M2 5h20v14H2z M4 7v.5l8 5 8-5V7l-8 5z" fill-rule="evenodd"/></svg>
          daniel@harwellpg.com.au
        </li>
        <li>
          <svg viewBox="0 0 24 24" aria-hidden="true"><path d="M12 2a10 10 0 1 0 0 20 10 10 0 0 0 0-20zm6.9 9h-3a15 15 0 0 0-1.3-5.6A8 8 0 0 1 18.9 11zM12 4.1c.9 1.3 1.7 3.8 1.9 6.9h-3.8c.2-3.1 1-5.6 1.9-6.9zM9.4 5.4A15 15 0 0 0 8.1 11h-3a8 8 0 0 1 4.3-5.6zM5.1 13h3a15 15 0 0 0 1.3 5.6A8 8 0 0 1 5.1 13zm6.9 6.9c-.9-1.3-1.7-3.8-1.9-6.9h3.8c-.2 3.1-1 5.6-1.9 6.9zm2.6-1.3a15 15 0 0 0 1.3-5.6h3a8 8 0 0 1-4.3 5.6z"/></svg>
          www.harwellpg.com.au
        </li>
      </ul>
      <p class="licence">Real Estate Lic: 1234567 &amp; 1234568</p>
    </div>
  </section>
</main>
</body>
</html>
```